Recycling Depot Business Card Design

We need a double sided business card for our recycling depot business. Please include name, position, address, phone, cell, fax, email and website address. Business card should match the colour scheme of our logo and look environmental but modern. I've attached a few business cards from Mintvale Works that I like.

Industry/Entity Type

Recycling

Contact Information for Business Card

Please include name, position, address, phone, cell, fax, email and website address.

Font styles to use
Sans Serif

Requirements
Must have
• Our Logo, Colour Scheme that matches our logo. Use of Colour Gradients and a custom look.

```html
<!DOCTYPE html>
<html lang="en">
<head>
<meta charset="utf-8">
<title>Greenloop Business Card</title>
<link rel="stylesheet" href="https://fonts.googleapis.com/css2?family=Open+Sans:wght@400;600;700;800&display=swap">
<style>
  :root {
    --bg: #e9ece9;
    --green-deep: #1f6b37;
    --green-mid: #2f8a3e;
    --green-light: #6cc04a;
    --green-pale: #c9e7b6;
    --ink-grey: #6d6e70;
    --white: #ffffff;
  }
  * { box-sizing: border-box; margin: 0; padding: 0; }
  html, body { width: 1200px; height: 900px; overflow: hidden; }
  body {
    background: var(--bg);
    font-family: "Open Sans", Arial, sans-serif;
    display: flex; flex-direction: column; align-items: center; justify-content: center;
    gap: 44px;
  }
  .card {
    width: 640px; height: 366px; border-radius: 26px; position: relative; overflow: hidden;
    box-shadow: 0 10px 30px rgba(0,0,0,0.18);
  }

  /* Back side */
  .card-back { background: var(--green-deep); }
  .back-brand {
    position: absolute; left: 0; right: 0; top: 104px;
    display: flex; align-items: center; justify-content: center; gap: 16px;
  }
  .brand-dot { width: 40px; height: 40px; border-radius: 50%; background: var(--green-light); }
  .back-brand .brand-name { color: var(--white); font-weight: 800; font-size: 64px; letter-spacing: -1px; }
  .back-band {
    position: absolute; left: 0; right: 0; top: 236px; height: 36px;
    background: linear-gradient(90deg, #5fb544, var(--green-light));
    display: flex; align-items: center; justify-content: center;
  }
  .back-band .address { color: var(--white); font-size: 15px; font-weight: 600; }

  /* Front side */
  .card-front { background: var(--white); }
  .front-brand { position: absolute; left: 44px; top: 54px; display: flex; align-items: center; gap: 12px; }
  .front-brand .brand-dot { width: 30px; height: 30px; background: var(--green-mid); }
  .front-brand .brand-name { color: var(--green-deep); font-weight: 800; font-size: 44px; letter-spacing: -1px; }
  .person { position: absolute; left: 98px; top: 172px; }
  .person-name { font-size: 30px; font-weight: 800; color: var(--green-deep); letter-spacing: -0.5px; line-height: 1; }
  .person-name .surname { color: var(--green-light); }
  .person-role { font-size: 16px; color: var(--ink-grey); margin-top: 6px; }
  .contact-list { list-style: none; margin-top: 14px; }
  .contact-list li { display: flex; align-items: center; gap: 12px; font-size: 15px; color: var(--ink-grey); line-height: 23px; }
  .contact-list svg { width: 16px; height: 16px; fill: var(--green-deep); flex: none; }
  .contact-list .web-domain { color: var(--green-deep); }
  .front-emblem {
    position: absolute; right: 56px; top: 70px; width: 210px; height: 210px; border-radius: 50%;
    background: radial-gradient(circle at 40% 35%, var(--green-pale), var(--green-light) 60%, var(--green-mid));
  }
</style>
</head>
<body>
  <section class="card card-back">
    <div class="back-brand">
      <span class="brand-dot"></span>
      <span class="brand-name">Greenloop</span>
    </div>
    <div class="back-band">
      <p class="address">1234 First Line Address 5678 Second Line Address</p>
    </div>
  </section>

  <section class="card card-front">
    <div class="front-brand">
      <span class="brand-dot"></span>
      <span class="brand-name">Greenloop</span>
    </div>
    <div class="person">
      <p class="person-name">NORA <span class="surname">ELLIS</span></p>
      <p class="person-role">Founder &amp; CEO</p>
      <ul class="contact-list">
        <li><svg viewBox="0 0 16 16"><path d="M1 5c0-2 2-3 7-3s7 1 7 3v1h-4V5H5v1H1zM3 7h10l1 7H2zm5 2a2 2 0 100 4 2 2 0 000-4z"/></svg>+100 5550 0142</li>
        <li><svg viewBox="0 0 16 16"><path d="M4 1h8v14H4zm1.5 1.5v9h5v-9zM8 12.5a.8.8 0 100 1.6.8.8 0 000-1.6z"/></svg>+100 5550 0143</li>
        <li><svg viewBox="0 0 16 16"><path d="M4 1h7v4H4zM1 6h14v6h-3v3H4v-3H1zm4 4v4h6v-4z"/></svg>+100 5550 0144</li>
        <li><svg viewBox="0 0 16 16"><path d="M1 3h14v10H1zm1.5 1.2v.3L8 9l5.5-4.5v-.3zM2.5 6.4v5.1h11V6.4L8 11z"/></svg>info@greenloopdepot.com</li>
        <li><svg viewBox="0 0 16 16"><path d="M8 1a7 7 0 100 14A7 7 0 008 1zm0 1.5c.8 0 1.8 1.8 2 4.5H6c.2-2.7 1.2-4.5 2-4.5zM2.6 7A5.5 5.5 0 015.4 3 9 9 0 004.5 7zm0 2h1.9a9 9 0 00.9 4A5.5 5.5 0 012.6 9zM6 9h4c-.2 2.7-1.2 4.5-2 4.5S6.2 11.7 6 9zm5.5 0h1.9a5.5 5.5 0 01-2.8 4 9 9 0 00.9-4zm0-2a9 9 0 00-.9-4 5.5 5.5 0 012.8 4z"/></svg>www.<span class="web-domain">greenloopdepot</span>.com</li>
      </ul>
    </div>
    <div class="front-emblem" role="img" aria-label="Space for the company emblem"></div>
  </section>
</body>
</html>
```